Dental Business Card

I need Dental oriented business cards.
On the front side -
- on the first line, my name:
Dr Marlo Vintner
- on the second line (just underneath):
Doctor of Dental Medicine
- on the third line, or underneath that or in a corner, I would like the address and phone number:
5182 Ch. Birchfield
Montreal QC H2T 4B9
514-629-5074
- other than that i would maybe like a logo of a tooth, but i want it to be subtle and very basic!
- I would like the card to be preferably black or dark grey-ish with the writing in white
On the other side -
- 2-3 lines with the possibility to write the next appointment the box with the lines should be white, with the rest of the card being black

```html
<!DOCTYPE html>
<html lang="en">
<head>
<meta charset="utf-8">
<title>Vintner Dental – Business Card</title>
<link rel="stylesheet" href="https://fonts.googleapis.com/css2?family=Open+Sans:wght@400;600;700;800&display=swap">
<style>
  :root {
    --stage: #2b2e33;
    --card: #0b0b0b;
    --ink: #ffffff;
    --ink-soft: #e6e6e6;
    --faint: #ececec;
    --rule: #0b0b0b;
  }
  * { margin: 0; padding: 0; box-sizing: border-box; }
  html, body {
    width: 1200px; height: 900px; overflow: hidden;
    background: var(--stage);
    font-family: "Open Sans", sans-serif;
  }
  .stage {
    width: 1200px; height: 900px;
    display: flex; align-items: center; justify-content: center; gap: 60px;
  }
  .card {
    width: 510px; height: 292px;
    background: var(--card);
    border-radius: 22px;
    position: relative;
    color: var(--ink);
    box-shadow: 0 10px 30px rgba(0,0,0,.35);
  }

  /* Back: appointment side */
  .appointment-title {
    position: absolute; top: 22px; left: 28px; right: 28px;
    display: flex; align-items: center; gap: 12px;
    font-weight: 800; font-size: 17px; letter-spacing: .4px; text-transform: uppercase;
  }
  .appointment-title::before, .appointment-title::after {
    content: ""; flex: 1; height: 2px; background: var(--ink);
  }
  .appointment-box {
    position: absolute; top: 58px; left: 28px; right: 28px; bottom: 26px;
    background: var(--ink); border-radius: 16px; overflow: hidden;
    display: flex; flex-direction: column;
  }
  .appointment-line { flex: 1; border-bottom: 3px solid var(--rule); }
  .appointment-line:last-child { border-bottom: none; }
  .appointment-watermark {
    position: absolute; inset: 0;
    display: flex; align-items: center; justify-content: center;
    font-weight: 700; font-size: 34px; color: var(--faint);
    pointer-events: none;
  }

  /* Front: identity side */
  .brand {
    position: absolute; left: 34px; top: 46px;
    display: flex; align-items: center; gap: 10px;
    font-weight: 700; font-size: 20px; color: var(--ink);
  }
  .brand-dot { width: 14px; height: 14px; border-radius: 50%; background: var(--ink); }
  .identity { position: absolute; left: 236px; top: 72px; }
  .identity-name { font-weight: 700; font-size: 22px; letter-spacing: .3px; }
  .identity-title { font-size: 15px; color: var(--ink-soft); margin-top: 1px; }
  .contact-list { list-style: none; margin-top: 18px; font-size: 14px; line-height: 1.35; }
  .contact-item { display: flex; align-items: flex-start; gap: 10px; margin-bottom: 6px; }
  .contact-icon { width: 16px; height: 16px; flex: none; margin-top: 2px; fill: var(--ink); }
</style>
</head>
<body>
<main class="stage">

  <section class="card card-back" aria-label="Appointment side">
    <h2 class="appointment-title">Next Appointment</h2>
    <div class="appointment-box">
      <div class="appointment-watermark" aria-hidden="true">Vintner Dental</div>
      <div class="appointment-line"></div>
      <div class="appointment-line"></div>
      <div class="appointment-line"></div>
      <div class="appointment-line"></div>
    </div>
  </section>

  <section class="card card-front" aria-label="Identity side">
    <div class="brand"><span class="brand-dot"></span>Vintner Dental</div>
    <div class="identity">
      <h1 class="identity-name">Dr MARLO VINTNER</h1>
      <p class="identity-title">Doctor of Dental Medicine</p>
      <ul class="contact-list">
        <li class="contact-item">
          <svg class="contact-icon" viewBox="0 0 24 24" aria-hidden="true"><path d="M6.6 10.8a15.1 15.1 0 0 0 6.6 6.6l2.2-2.2a1 1 0 0 1 1-.25 11.4 11.4 0 0 0 3.6.57 1 1 0 0 1 1 1V20a1 1 0 0 1-1 1A17 17 0 0 1 3 4a1 1 0 0 1 1-1h3.5a1 1 0 0 1 1 1c0 1.25.2 2.45.57 3.57a1 1 0 0 1-.25 1z"/></svg>
          <span>514-629-5074</span>
        </li>
        <li class="contact-item">
          <svg class="contact-icon" viewBox="0 0 24 24" aria-hidden="true"><path d="M2 5h20v14H2z" fill="none"/><path d="M2 5h20l-10 7z"/><path d="M2 7.5l10 7 10-7V19H2z"/></svg>
          <span>hello@vintnerdental.ca</span>
        </li>
        <li class="contact-item">
          <svg class="contact-icon" viewBox="0 0 24 24" aria-hidden="true"><path d="M12 2a7 7 0 0 0-7 7c0 5.2 7 13 7 13s7-7.8 7-13a7 7 0 0 0-7-7zm0 9.5A2.5 2.5 0 1 1 12 6.5a2.5 2.5 0 0 1 0 5z"/></svg>
          <span>5182 Ch. Birchfield<br>Montreal QC H2T 4B9</span>
        </li>
      </ul>
    </div>
  </section>

</main>
</body>
</html>
```